Kestrel Summit 2019 Enemies of the End-Times Church Flyer

We want a church conference flyer designed. We are looking for a professional, yet catchy design that uses our brand colors and logo creatively while communicating key information of the event effectively. <br/>The flyer must include all of the following:<br/>Title: Kestrel Summit 2019<br/>Topic: The Enemies of The End-Times Church <br/>Subtitles: <br/> -How the antichrist raises an army by social behavior engineering. <br/>-How the architects of modern social constructs escaped the church's radar. <br/>-The Holy Spirit's end-times agenda:<br/> The Knock-Out Punch!<br/>Speaker: Prophet Marcus Toliver <br/>Dates/time: December 27, 28 & 29 at 6pm<br/>Location: Halvorn Community Center <br/> 241 Pellham Street <br/> Portland, ME 04102<br/>Contact info: phone: 207-555-0148 <br/>email: contact@brookmeadow.example <br/> www.vutel.example<br/>*The flyer must also include a picture of the speaker and our Vutel logo <br/>Thanks, we look forward to seeing what you come up with!

Colors

Designer to choose colors to be used in the design.

Requirements
Must have
• The flyer must include all of the following:
• Title: Kestrel Summit 2019
• Topic: The Enemies of The End-Times Church
• Subtitles:
• -How the antichrist raises an army by social behavior engineering.
• -How the architects of modern social constructs escaped the church's radar.
• -The Holy Spirit's end-times agenda:
• The Knock-Out Punch!
• Speaker: Prophet Marcus Toliver
• Dates/time: December 27, 28 & 29 at 6pm
• Location: Halvorn Community Center
• 241 Pellham Street
• Portland, ME 04102
• Contact info: phone: 207-555-0148
• email: contact@brookmeadow.example
• www.vutel.example
• *The flyer must also include a picture of the speaker and our Vutel logo
Should not have
• Pictures of crosses or church buildings

```html
<!DOCTYPE html>
<html lang="en">
<head>
<meta charset="utf-8">
<title>Kestrel Summit 2019 – Flyer</title>
<link rel="stylesheet" href="https://fonts.googleapis.com/css2?family=Montserrat:wght@700;800&family=Didact+Gothic&family=Saira+Condensed:wght@400;500;600;700&family=Comfortaa:wght@600&display=swap">
<style>
  :root{
    --backdrop:#e37302;
    --paper:#f4f4f5;
    --navy:#0f3556;
    --navy-deep:#0b2a45;
    --teal:#174b5c;
    --orange:#f0891f;
    --orange-light:#f7ac30;
    --rust:#c6452a;
    --white:#ffffff;
  }
  *{margin:0;padding:0;box-sizing:border-box}
  html,body{width:1200px;height:1200px;overflow:hidden;background:var(--backdrop)}
  .flyer{position:absolute;left:230px;top:75px;width:740px;height:1050px;
    background:radial-gradient(ellipse at 50% 45%,#ffffff 0%,var(--paper) 60%,#e6e6e8 100%);overflow:hidden}
  .swoosh{position:absolute;left:0;top:0;width:740px;height:1050px}
  .brand{position:absolute;left:556px;top:64px;display:flex;align-items:center;gap:8px;
    font-family:"Montserrat",sans-serif;font-weight:700;font-size:34px;color:var(--navy);letter-spacing:1px}
  .brand-dot{width:14px;height:14px;border-radius:50%;background:var(--orange)}
  .title{position:absolute;left:0;width:740px;text-align:center;font-family:"Montserrat",sans-serif;
    font-weight:800;color:var(--navy);line-height:1}
  .title-top{top:115px;font-size:80px;letter-spacing:3px;padding-left:0;left:-14px}
  .title-main{top:194px;font-size:80px;letter-spacing:2px;left:8px}
  .year{position:absolute;top:268px;left:0;width:740px;text-align:center;font-family:"Didact Gothic",sans-serif;
    font-size:88px;color:var(--navy);line-height:1;padding-left:24px}
  .rule{position:absolute;top:319px;height:1px;background:linear-gradient(90deg,transparent,var(--orange))}
  .rule-left{left:54px;width:196px}
  .rule-right{left:484px;width:198px;background:linear-gradient(90deg,var(--orange),transparent)}
  .topic{position:absolute;top:372px;left:0;width:740px;text-align:center;font-family:"Saira Condensed",sans-serif;
    font-weight:500;font-size:42px;color:var(--navy);line-height:1;padding-left:32px}
  .agenda{position:absolute;left:0;top:430px;width:680px;height:142px;
    background:linear-gradient(90deg,var(--orange-light) 0%,#e8762a 45%,var(--rust) 100%);
    padding:12px 0 0 64px;list-style:none}
  .agenda li{font-family:"Saira Condensed",sans-serif;font-weight:600;font-size:20px;color:var(--white);
    height:32.5px;line-height:28px;border-bottom:1px solid rgba(255,255,255,.45);width:max-content;padding-right:10px}
  .agenda li:last-child{border-bottom:none}
  .speaker-photo{position:absolute;left:418px;top:573px;width:322px;height:384px}
  .info{position:absolute;left:64px;width:380px;text-align:center;font-family:"Saira Condensed",sans-serif;color:var(--navy)}
  .pin{position:absolute;left:238px;top:602px;width:40px;height:40px}
  .venue{top:652px;font-size:27px;font-weight:600;line-height:1}
  .address{top:684px;font-size:20px;font-weight:600;line-height:1}
  .speaker{position:absolute;left:64px;top:721px;width:380px;height:37px;border:1.5px solid var(--orange);
    font-family:"Saira Condensed",sans-serif;font-weight:600;font-size:25px;color:var(--orange);
    text-align:center;line-height:34px}
  .label{font-family:"Didact Gothic",sans-serif;font-size:24px;line-height:1}
  .dates-label{top:771px}
  .dates{top:790px;font-size:46px;font-weight:700;line-height:1;letter-spacing:-.5px}
  .time-label{top:842px}
  .time{top:866px;font-size:46px;font-weight:700;line-height:1}
  .phone-icon{position:absolute;left:79px;top:937px;width:42px;height:42px}
  .phone{position:absolute;left:39px;top:983px;font-family:"Saira Condensed",sans-serif;font-weight:700;
    font-size:29px;color:var(--navy);line-height:1}
  .contact{position:absolute;right:32px;top:976px;text-align:right;font-family:"Comfortaa",sans-serif;
    font-weight:600;font-size:14px;color:var(--white);line-height:20px}
  .contact span{display:flex;align-items:center;justify-content:flex-end;gap:10px}
  .contact svg{width:14px;height:14px}
</style>
</head>
<body>
<main class="flyer">
  <svg class="swoosh" viewBox="0 0 740 1050" aria-hidden="true">
    <defs>
      <linearGradient id="orangeBand" x1="0" y1="0" x2="1" y2="0">
        <stop offset="0" stop-color="#f39a2a"/><stop offset="1" stop-color="#d9531f"/>
      </linearGradient>
      <linearGradient id="orangeSoft" x1="0" y1="1" x2="1" y2="0">
        <stop offset="0" stop-color="#f7b144"/><stop offset="1" stop-color="#ee8a22"/>
      </linearGradient>
      <linearGradient id="navyBand" x1="0" y1="0" x2="1" y2="1">
        <stop offset="0" stop-color="#184c5e"/><stop offset="1" stop-color="#0b2a45"/>
      </linearGradient>
    </defs>
    <!-- top-left corner -->
    <path d="M0 0 H560 C390 10 150 90 0 240 Z" fill="url(#navyBand)"/>
    <path d="M0 285 C110 120 300 30 540 6 C330 40 120 150 0 250 Z" fill="url(#orangeSoft)"/>
    <path d="M0 240 C140 95 360 15 610 0 H520 C330 25 130 100 0 210 Z" fill="url(#orangeBand)"/>
    <path d="M380 18 C480 6 560 2 610 0 H700 C600 6 480 12 380 18 Z" fill="#0b2a45"/>
    <!-- band below agenda -->
    <path d="M0 572 H620 L0 597 Z" fill="var(--navy)"/>
    <!-- bottom-right corner -->
    <path d="M740 715 C640 860 420 990 60 1050 H200 C470 1000 660 900 740 800 Z" fill="url(#orangeSoft)"/>
    <path d="M740 790 C650 900 460 1000 160 1050 H740 Z" fill="url(#orangeBand)"/>
    <path d="M740 875 C640 960 480 1020 300 1050 H740 Z" fill="url(#navyBand)"/>
  </svg>

  <div class="brand"><span class="brand-dot"></span>VUTEL</div>

  <h1>
    <span class="title title-top">KESTREL</span>
    <span class="title title-main">SUMMIT</span>
  </h1>
  <div class="rule rule-left"></div>
  <div class="year">2019</div>
  <div class="rule rule-right"></div>
  <h2 class="topic">The Enemies of The End-Times Church</h2>

  <ul class="agenda">
    <li>How the antichrist raises an army by social behavior engineering.</li>
    <li>How the architects of modern social constructs escaped the church's radar.</li>
    <li style="width:360px">The Holy Spirit's end-times agenda:</li>
    <li>The Knock-Out Punch!</li>
  </ul>

  <div class="speaker-photo" role="img" aria-label="Photo of speaker Prophet Marcus Toliver"
       style="background:linear-gradient(160deg,rgba(244,244,245,0) 0%,#3d3f46 35%,#6e2a2c 60%,#2a2c33 100%);clip-path:polygon(30% 0,62% 0,80% 30%,96% 55%,100% 100%,0 100%,8% 70%,28% 40%)"></div>

  <svg class="pin" viewBox="0 0 40 40" aria-hidden="true" fill="none" stroke="var(--orange)" stroke-width="3">
    <path d="M20 30 C12 20 9 16 9 12 a11 11 0 0 1 22 0 c0 4 -3 8 -11 18 Z"/>
    <circle cx="20" cy="12" r="4"/>
    <path d="M12 26 H6 L2 38 H38 L34 26 H28"/>
  </svg>
  <div class="info venue">Halvorn Community Center</div>
  <div class="info address">241 Pellham Street | Portland, ME 04102</div>

  <div class="speaker">Speaker: Prophet Marcus Toliver</div>

  <div class="info label dates-label">Dates</div>
  <div class="info dates">December 27, 28 &amp; 29</div>
  <div class="info label time-label">Time</div>
  <div class="info time">6pm</div>

  <svg class="phone-icon" viewBox="0 0 42 42" aria-hidden="true" fill="none" stroke="var(--navy-deep)" stroke-width="2">
    <circle cx="21" cy="21" r="19.5"/>
    <path d="M14 11 l4 5 -2 3 c1 3 4 6 7 7 l3 -2 5 4 -2 3 c-8 1 -18 -9 -17 -17 Z"/>
  </svg>
  <div class="phone">207-555-0148</div>

  <div class="contact">
    <span>contact@brookmeadow.example
      <svg viewBox="0 0 14 14" fill="none" stroke="#fff" stroke-width="1"><rect x="1" y="3" width="12" height="8"/><path d="M1 3 L7 8 L13 3"/></svg></span>
    <span>www.vutel.example
      <svg viewBox="0 0 14 14" fill="none" stroke="#fff" stroke-width="1"><circle cx="7" cy="7" r="6"/><ellipse cx="7" cy="7" rx="2.6" ry="6"/><path d="M1 7 H13 M2 4 H12 M2 10 H12"/></svg></span>
  </div>
</main>
</body>
</html>
```